Gale Sentry - WEBSITE Contest - 4-5 pages coding - Strong, simple clean WORDPRESS

Hello,
The inspiriation website is www.brixhalo.com
Please look at this site because I want to copy that.
I have changed the order a little bit so please look at my order of the site elements.
I will supply text, please just use lorem ipsum for now.
PLEASE LOOK AT THE BRIX HALO WEBSITE AND MAKE A COPY OF THAT.
PPlease look at that site and see the different features it has and make that.
We will need this main page and then:
-About Us page
-Contact Us page
-Request a quote page / fillable form
-1 product/service page
Thank you,
Trevor
/////////////////////////////
Website design for Gale Sentry.
Please design with simple, easy to read fonts. Customers are older and need strong, bold easy to read.
galesentry-demo.com
Tel (555) 318-4072
trevor@galesentry-demo.com
The problem is that all roofing vents leak. We have a product that goes into the vent that stops the roof from leaking.
Your beautiful Florida home is unprotected!
All roof vents leak!
Winds over 30 MPH push rainwater INTO your home through the rooftop vents! The result is water damage that can cost thousands of dollars to repair and remediate!
The GALE SENTRY is a powerful roof vent protection system, engineered to block wind driven rains from entering your home's roof vents.
The Gale Sentry is made to withstand extreme conditions. Featuring IMPACT hurricane screening and powerful steel construction.
Professional installation is permanent and concealed and is accomplished via the roof top.
Get protected for all the storms ahead! Get the Gale Sentry!
www.galesentry-demo.com
Call Now: 555 318-4072
Updates
Hello to all designers - please add a "SERVICE AREA MAP" widget to the designs. Thank you.
Target Market(s)
The target customer is a affluent, older couple 50-60 years old. Homeowner. middle class to upper class adults / ages 50-60 years old (older but not VERY old)
Industry/Entity Type
roofing and construction
Coding
Coded - Design and coding required
Number of Pages Required
4 page
Colors
Designer to choose colors to be used in the design.
Requirements
Must have
- Great landing page, about us page, product page, contact us page, request quote form / Strong, simple clean
Nice to have
- feelings: professional / strong / reliable / safety / shelter / security / future stability/ calm / security
Should not have
- stress / fear feeling - this product will remove fear and stress of damages from storms

```html
<!DOCTYPE html>
<html lang="en">
<head>
<meta charset="utf-8">
<title>Gale Sentry – Roof Vent Protection</title>
<link rel="stylesheet" href="https://fonts.googleapis.com/css2?family=Poppins:wght@400;600;700&family=Open+Sans:wght@400;600;700&display=swap">
<style>
:root{
  --blue:#0a6aa8;
  --blue-dark:#074c7c;
  --teal:#1aa6c9;
  --ink:#2b2b2b;
  --muted:#666;
  --light:#eef1f4;
  --footer:#1e1f21;
  --footer-deep:#151617;
  --white:#fff;
}
*{box-sizing:border-box;margin:0;padding:0}
html,body{width:1200px;height:3560px;overflow:hidden}
body{font-family:"Open Sans",Arial,sans-serif;color:var(--ink);background:var(--white);position:relative}
h1,h2,h3,h4,.btn,.nav a{font-family:"Poppins",Arial,sans-serif}
.btn{display:inline-block;background:var(--teal);color:var(--white);font-weight:600;font-size:14px;letter-spacing:.5px;padding:12px 30px;border-radius:24px;text-decoration:none}
.btn-sm{font-size:11px;padding:7px 16px;border-radius:16px}
.section-title{text-align:center;font-size:30px;font-weight:700;letter-spacing:1px}
.section-title::after{content:"";display:block;width:60px;height:3px;background:var(--teal);margin:12px auto 0}

/* header */
.site-header{position:absolute;top:0;left:0;width:1200px;height:74px;background:var(--white);display:flex;align-items:center;padding:0 60px;z-index:2;box-shadow:0 2px 6px rgba(0,0,0,.12)}
.brand{display:flex;align-items:center;gap:10px;color:var(--blue);font-family:"Poppins",sans-serif;font-weight:700;font-size:22px}
.brand-dot{width:34px;height:34px;border-radius:50%;background:var(--blue)}
.nav{margin-left:auto;display:flex;gap:30px}
.nav a{font-size:14px;font-weight:600;color:var(--ink);text-decoration:none}
.nav a.active{color:var(--teal)}
.header-call{margin-left:50px;display:flex;align-items:center;gap:10px}
.header-call small{display:block;font-size:11px;color:var(--muted)}
.header-call strong{font-family:"Poppins",sans-serif;font-size:20px;color:var(--blue)}

/* hero */
.hero{position:absolute;top:0;left:0;width:1200px;height:560px;background:linear-gradient(160deg,#8f969c 0%,#c6ccd1 40%,#7d858c 75%,#5b6369 100%);text-align:center;color:var(--white)}
.hero h1{position:absolute;top:240px;width:100%;font-size:38px;font-weight:700;line-height:1.3;text-shadow:0 2px 6px rgba(0,0,0,.5)}
.hero .btn{position:absolute;top:360px;left:538px}
.hero-dots{position:absolute;top:520px;left:0;width:100%;display:flex;justify-content:center;gap:8px}
.hero-dots span{width:10px;height:10px;border-radius:50%;background:rgba(255,255,255,.6)}
.hero-dots span.on{background:var(--white)}

/* welcome */
.welcome{position:absolute;top:560px;left:0;width:1200px;height:440px;display:flex;align-items:center;padding:0 110px;gap:90px}
.welcome-mark{width:360px;height:340px;display:flex;flex-direction:column;align-items:center;justify-content:center;gap:18px}
.welcome-mark .circle{width:230px;height:230px;border-radius:50%;background:var(--blue)}
.welcome-mark span{font-family:"Poppins",sans-serif;font-weight:700;font-size:32px;color:var(--blue)}
.welcome-text{width:520px}
.welcome-text h3{color:var(--teal);font-size:22px;font-weight:600}
.welcome-text h2{color:var(--blue);font-size:36px;font-weight:700;margin:2px 0 8px}
.welcome-text h2::after{content:"";display:block;width:60px;height:3px;background:var(--teal);margin-top:10px}
.welcome-text p{font-size:15px;line-height:1.75;color:var(--muted);margin:16px 0 24px}

/* services */
.services{position:absolute;top:1000px;left:0;width:1200px;height:500px;background:linear-gradient(180deg,var(--blue) 0%,var(--blue-dark) 100%);color:var(--white);padding-top:55px}
.service-grid{display:grid;grid-template-columns:1fr 1fr;gap:55px 80px;padding:55px 130px 0}
.service{display:flex;gap:24px}
.service-icon{flex:0 0 88px;height:88px;border:2px solid rgba(255,255,255,.8);border-radius:50%;display:flex;align-items:center;justify-content:center}
.service h4{font-size:16px;font-weight:700;margin-bottom:6px}
.service p{font-size:13px;line-height:1.6;opacity:.9;margin-bottom:10px}

/* why */
.why{position:absolute;top:1500px;left:0;width:1200px;height:500px;background:var(--light);padding-top:50px}
.why .section-title{color:var(--blue-dark)}
.why-body{display:flex;align-items:center;justify-content:center;gap:40px;margin-top:40px}
.why-col{width:320px;display:flex;flex-direction:column;gap:60px}
.why-item{display:flex;gap:16px;align-items:flex-start}
.why-icon{flex:0 0 56px;height:56px;border-radius:50%;background:var(--blue);display:flex;align-items:center;justify-content:center}
.why-item p{font-size:13px;line-height:1.6;color:var(--muted)}
.why-photo{width:300px;height:300px;border-radius:50%;background:radial-gradient(circle at 45% 40%,#d7dadd 0%,#8c9398 55%,#3c4146 100%)}

/* testimonials */
.testimonials{position:absolute;top:2000px;left:0;width:1200px;height:480px;padding-top:50px}
.testimonials .section-title{color:var(--blue-dark)}
.cards{display:flex;justify-content:center;gap:40px;margin-top:45px;position:relative}
.card{width:290px;height:290px;border:1px solid #c9d3dc;text-align:center;padding:26px 26px}
.card .quote{font-family:"Poppins",sans-serif;font-size:48px;line-height:.8;color:var(--blue);height:34px}
.card p{font-size:13px;line-height:1.65;color:var(--muted);margin-top:10px}
.card h4{font-size:13px;color:var(--blue);margin-top:14px;font-weight:600}
.arrow{position:absolute;top:135px}
.arrow.left{left:70px}.arrow.right{right:70px}

/* contact */
.contact{position:absolute;top:2480px;left:0;width:1200px;height:520px;background:linear-gradient(160deg,#0d3f6b 0%,#0a5a93 50%,#083a63 100%);color:var(--white);padding-top:50px}
.contact-form{width:640px;margin:40px auto 0;display:grid;grid-template-columns:1fr 1fr;gap:16px}
.field{background:var(--white);height:40px;padding:0 14px;font-size:13px;color:#888;display:flex;align-items:center}
.field.full{grid-column:1/3}
.field.msg{height:130px;align-items:flex-start;padding-top:12px}
.contact-form .btn{grid-column:1/3;justify-self:center;padding:12px 54px;margin-top:6px}

/* footer */
.site-footer{position:absolute;top:3000px;left:0;width:1200px;height:500px;background:var(--footer);color:#cfd2d5;display:flex;padding:60px 80px 0;gap:60px}
.footer-brand{width:250px;display:flex;align-items:center;gap:12px;color:var(--white);font-family:"Poppins",sans-serif;font-weight:700;font-size:24px;align-self:flex-start;margin-top:10px}
.footer-brand .brand-dot{width:46px;height:46px;background:var(--teal)}
.footer-col h4{color:var(--white);font-size:15px;font-weight:600;margin-bottom:22px}
.footer-col.contact-col{width:330px}
.footer-col.menu-col{width:170px}
.footer-line{display:flex;gap:12px;align-items:flex-start;font-size:13px;line-height:1.55;margin-bottom:18px}
.footer-ico{flex:0 0 32px;height:32px;border-radius:50%;background:#3a3c3f;display:flex;align-items:center;justify-content:center}
.menu-col ul{list-style:none;font-size:13px;line-height:2}
.social-dot{flex:0 0 32px;height:32px;border-radius:50%;background:#3a3c3f}
.copyright{position:absolute;top:3500px;left:0;width:1200px;height:60px;background:var(--footer-deep);color:#9a9da0;font-size:12px;display:flex;align-items:center;justify-content:center}
</style>
</head>
<body>

<header class="site-header">
  <div class="brand"><span class="brand-dot"></span>GALE SENTRY</div>
  <nav class="nav">
    <a class="active" href="#">HOME</a><a href="#">ABOUT US</a><a href="#">SERVICES</a><a href="#">BLOG</a><a href="#">CONTACT US</a>
  </nav>
  <div class="header-call">
    <svg width="26" height="26" viewBox="0 0 24 24"><path fill="#0a6aa8" d="M6.6 10.8a15.1 15.1 0 0 0 6.6 6.6l2.2-2.2c.3-.3.7-.4 1-.2 1.1.4 2.3.6 3.6.6.6 0 1 .4 1 1V20c0 .6-.4 1-1 1A17 17 0 0 1 3 4c0-.6.4-1 1-1h3.5c.6 0 1 .4 1 1 0 1.3.2 2.5.6 3.6.1.3 0 .7-.2 1z"/></svg>
    <div><small>Call Us</small><strong>555 318-4072</strong></div>
  </div>
</header>

<section class="hero" role="img" aria-label="Photo of a steel roof vent protection unit installed on a rooftop">
  <h1>GET PROTECTED FOR ALL THE STORMS AHEAD!<br>GET THE GALE SENTRY!</h1>
  <a class="btn" href="#">READ MORE</a>
  <div class="hero-dots"><span class="on"></span><span></span><span></span></div>
</section>

<section class="welcome">
  <div class="welcome-mark"><div class="circle"></div><span>GALE SENTRY</span></div>
  <div class="welcome-text">
    <h3>WELCOME TO</h3>
    <h2>GALE SENTRY</h2>
    <p>There are many variations of passages of Lorem Ipsum available, but the majority have suffered alteration in some form, by injected humour, or randomised words which don't look even slightly believable. If you are going to use a passage of Lorem Ipsum, you need to be sure there isn't anything embarrassing hidden in the middle of text. All the Lorem Ipsum generators on the Internet tend to repeat predefined chunks as necessary.</p>
    <a class="btn btn-sm" href="#">READ MORE</a>
  </div>
</section>

<section class="services">
  <h2 class="section-title">OUR SERVICES</h2>
  <div class="service-grid">
    <div class="service">
      <div class="service-icon"><svg width="44" height="44" viewBox="0 0 44 44" fill="none" stroke="#fff" stroke-width="2"><rect x="6" y="12" width="32" height="22" rx="2"/><path d="M6 20h32M6 27h32M16 12v22M28 12v22"/></svg></div>
      <div><h4>LOREM IPSUM IS SIMPLY</h4><p>There are many variations of passages of Lorem Ipsum available, but the majority have suffered alteration in some form anything.</p><a class="btn btn-sm" href="#">READ MORE</a></div>
    </div>
    <div class="service">
      <div class="service-icon"><svg width="44" height="44" viewBox="0 0 44 44" fill="none" stroke="#fff" stroke-width="2"><path d="M22 6a16 16 0 1 0 16 16"/><path d="M22 14a8 8 0 1 0 8 8"/><circle cx="22" cy="22" r="2"/></svg></div>
      <div><h4>LOREM IPSUM IS SIMPLY</h4><p>There are many variations of passages of Lorem Ipsum available, but the majority have suffered alteration in some form anything.</p><a class="btn btn-sm" href="#">READ MORE</a></div>
    </div>
    <div class="service">
      <div class="service-icon"><svg width="44" height="44" viewBox="0 0 44 44" fill="none" stroke="#fff" stroke-width="2"><path d="M6 22 22 8l16 14"/><path d="M11 18v18h22V18"/><rect x="19" y="26" width="6" height="10"/></svg></div>
      <div><h4>LOREM IPSUM IS SIMPLY</h4><p>There are many variations of passages of Lorem Ipsum available, but the majority have suffered alteration in some form anything.</p><a class="btn btn-sm" href="#">READ MORE</a></div>
    </div>
    <div class="service">
      <div class="service-icon"><svg width="44" height="44" viewBox="0 0 44 44" fill="none" stroke="#fff" stroke-width="2"><path d="M22 6 36 11v10c0 9-6 15-14 17C14 36 8 30 8 21V11z"/><path d="m16 22 5 5 8-9"/></svg></div>
      <div><h4>LOREM IPSUM IS SIMPLY</h4><p>There are many variations of passages of Lorem Ipsum available, but the majority have suffered alteration in some form anything.</p><a class="btn btn-sm" href="#">READ MORE</a></div>
    </div>
  </div>
</section>

<section class="why">
  <h2 class="section-title">WHY CHOOSE US</h2>
  <div class="why-body">
    <div class="why-col">
      <div class="why-item"><div class="why-icon"><svg width="26" height="26" viewBox="0 0 24 24" fill="none" stroke="#fff" stroke-width="2"><path d="M3 12 12 4l9 8M6 10v10h12V10"/></svg></div><p>Winds over 30 MPH push rainwater INTO your home through the rooftop vents! The result is water damage that can cost thousands of dollars to repair and remediate!</p></div>
      <div class="why-item"><div class="why-icon"><svg width="26" height="26" viewBox="0 0 24 24" fill="none" stroke="#fff" stroke-width="2"><path d="M12 3 20 6v6c0 5-3.5 8-8 9-4.5-1-8-4-8-9V6z"/></svg></div><p>The GALE SENTRY is a powerful roof vent protection system, engineered to block wind driven rains from entering your home's roof vents.</p></div>
    </div>
    <div class="why-photo" role="img" aria-label="Close-up photo of a round roof vent with protective screen"></div>
    <div class="why-col">
      <div class="why-item"><div class="why-icon"><svg width="26" height="26" viewBox="0 0 24 24" fill="none" stroke="#fff" stroke-width="2"><path d="M4 8h11a3 3 0 1 0-3-3M4 12h15a3 3 0 1 1-3 3M4 16h7"/></svg></div><p>The Gale Sentry is made to withstand extreme conditions. Featuring IMPACT hurricane screening and powerful steel construction.</p></div>
      <div class="why-item"><div class="why-icon"><svg width="26" height="26" viewBox="0 0 24 24" fill="none" stroke="#fff" stroke-width="2"><path d="m5 12 5 5 9-10"/></svg></div><p>Professional installation is permanent and concealed and is accomplished via the roof top.</p></div>
    </div>
  </div>
</section>

<section class="testimonials">
  <h2 class="section-title">TESTIMONIALS</h2>
  <div class="cards">
    <svg class="arrow left" width="20" height="30" viewBox="0 0 20 30"><path d="M16 3 4 15l12 12" fill="none" stroke="#0a6aa8" stroke-width="3"/></svg>
    <article class="card"><div class="quote">&ldquo;</div><p>There are many variations of passages of Lorem Ipsum available, but the majority have suffered alteration in some form, by injected humour, or randomised words which don't look even slightly believable. If you are going to use a passage of Lorem Ipsum, you need to be sure.</p><h4>DIANA</h4></article>
    <article class="card"><div class="quote">&ldquo;</div><p>There are many variations of passages of Lorem Ipsum available, but the majority have suffered alteration in some form, by injected humour, or randomised words which don't look even slightly believable. If you are going to use a passage of Lorem Ipsum, you need to be sure.</p><h4>DIANA</h4></article>
    <article class="card"><div class="quote">&ldquo;</div><p>There are many variations of passages of Lorem Ipsum available, but the majority have suffered alteration in some form, by injected humour, or randomised words which don't look even slightly believable. If you are going to use a passage of Lorem Ipsum, you need to be sure.</p><h4>DIANA</h4></article>
    <svg class="arrow right" width="20" height="30" viewBox="0 0 20 30"><path d="M4 3l12 12L4 27" fill="none" stroke="#0a6aa8" stroke-width="3"/></svg>
  </div>
</section>

<section class="contact">
  <h2 class="section-title">CONTACT US</h2>
  <form class="contact-form">
    <div class="field">First Name</div>
    <div class="field">Last Name</div>
    <div class="field">Email Id</div>
    <div class="field">Phone</div>
    <div class="field full msg">Message</div>
    <a class="btn" href="#">SUBMIT</a>
  </form>
</section>

<footer class="site-footer">
  <div class="footer-brand"><span class="brand-dot"></span>GALE SENTRY</div>
  <div class="footer-col contact-col">
    <h4>CONTACT US</h4>
    <div class="footer-line"><span class="footer-ico"><svg width="14" height="16" viewBox="0 0 14 18"><path fill="#fff" d="M7 0a7 7 0 0 0-7 7c0 5 7 11 7 11s7-6 7-11a7 7 0 0 0-7-7zm0 9.5A2.5 2.5 0 1 1 7 4.5a2.5 2.5 0 0 1 0 5z"/></svg></span><span>Suite 210, 88 Harbor Lane,<br>Port Vale FL 30000</span></div>
    <div class="footer-line"><span class="footer-ico"><svg width="14" height="14" viewBox="0 0 24 24"><path fill="#fff" d="M6.6 10.8a15.1 15.1 0 0 0 6.6 6.6l2.2-2.2c.3-.3.7-.4 1-.2 1.1.4 2.3.6 3.6.6.6 0 1 .4 1 1V20c0 .6-.4 1-1 1A17 17 0 0 1 3 4c0-.6.4-1 1-1h3.5c.6 0 1 .4 1 1 0 1.3.2 2.5.6 3.6.1.3 0 .7-.2 1z"/></svg></span><span>Call Us<br>(555) 318-4072</span></div>
    <div class="footer-line"><span class="footer-ico"><svg width="15" height="12" viewBox="0 0 20 14"><rect x="1" y="1" width="18" height="12" fill="none" stroke="#fff" stroke-width="2"/><path d="m1 1 9 7 9-7" fill="none" stroke="#fff" stroke-width="2"/></svg></span><span>Email Us<br>trevor@galesentry-demo.com</span></div>
  </div>
  <div class="footer-col menu-col">
    <h4>MENU</h4>
    <ul><li>HOME</li><li>ABOUT US</li><li>SERVICES</li><li>BLOG</li><li>CONTACT US</li></ul>
  </div>
  <div class="footer-col">
    <h4>FOLLOW US</h4>
    <div class="footer-line"><span class="social-dot"></span><span>Follow us on<br>our news</span></div>
    <div class="footer-line"><span class="social-dot"></span><span>Follow us on<br>our updates</span></div>
    <div class="footer-line"><span class="social-dot"></span><span>Follow us on<br>our network</span></div>
  </div>
</footer>
<div class="copyright">Copyright © 2016 All Rights Reserved</div>

</body>
</html>
```